Business card design for crowd sourced review site.

I need a business card magnet design for an online, crowd-sourced, restaurant review site strictly for Kosher restaurants.
It is similar to RoamLedger but catering to a very particular crowd.
The markets it will be distributed in are flooded with business card fridge magnets so this needs to be eye-catching and unique. The Business name is PlateMarks
The website isnt finished but you can see the basic setup here
http://restaurant.vintrello.com/

The second image i included is another logo design I liked and was thinking about using and decided I will probably also make a SECOND custom cut business card in the shape of that icon. Bonus if you can throw that in also.

Target Market(s)

Jewish consumers aged 20-35

Industry/Entity Type

Business

Contact Information for Business Card

see description.
Design should not be too crowded and should in eye-catching. Will mainly be used as fridge magnets.

Requirements
Must have
• Website address. logo.
Nice to have
• tagline. (Honest kosher restaurant reviews, written by people who dine out)
• Im not a professional but I personally think the color blue goes along with this concept. ill leave it to you to decide.
Should not have
• any religious symbols.

```html
<!DOCTYPE html>
<html lang="en">
<head>
<meta charset="utf-8">
<title>PlateMarks business card</title>
<link href="https://fonts.googleapis.com/css2?family=Source+Sans+3:ital,wght@0,400;0,600;1,400&display=swap" rel="stylesheet">
<style>
  :root {
    --backdrop: #5a493c;
    --card: #000000;
    --red: #d93224;
    --red-bright: #e8261c;
    --red-dark: #a82016;
    --white: #ffffff;
    --text-light: #e6e6e6;
    --text-dark: #1a1a1a;
    --divider: #4a4a4a;
  }
  * { margin: 0; padding: 0; box-sizing: border-box; }
  html, body {
    width: 1200px; height: 987px; overflow: hidden;
    background: var(--backdrop);
    font-family: "Source Sans 3", "Myriad Pro", sans-serif;
  }
  .canvas { position: relative; width: 1200px; height: 987px; }
  .card {
    position: absolute; left: 293px; width: 615px; height: 350px;
    background: var(--card); overflow: hidden;
  }
  .card--front { top: 130px; }
  .card--back { top: 505px; }

  .brand {
    position: absolute; left: 56px; top: 150px;
    display: flex; align-items: center; gap: 10px;
  }
  .brand__dot { width: 22px; height: 22px; border-radius: 50%; background: var(--red); }
  .brand__name { color: var(--white); font-size: 32px; font-weight: 600; line-height: 1; }

  .divider {
    position: absolute; left: 319px; top: 53px; width: 1px; height: 222px;
    background: linear-gradient(to bottom, transparent, var(--divider) 20%, var(--divider) 80%, transparent);
  }
  .contact { position: absolute; left: 346px; top: 58px; color: var(--text-light); }
  .contact__name { color: var(--red); font-size: 22px; font-weight: 600; line-height: 26px; }
  .contact__role { font-size: 17px; line-height: 22px; }
  .contact__address { margin-top: 10px; font-size: 16.5px; line-height: 22px; }
  .contact__list { list-style: none; margin-top: 6px; }
  .contact__item { display: flex; align-items: center; gap: 8px; font-size: 16.5px; line-height: 23.5px; }
  .contact__item svg { width: 15px; height: 15px; fill: var(--red); flex: none; }

  .band {
    position: absolute; left: 0; top: 306px; width: 527px; height: 29px;
    background: var(--red); border-bottom: 2px solid var(--red-dark);
  }
  .band__url {
    position: absolute; left: 118px; top: 3px;
    color: var(--text-dark); font-size: 17px; letter-spacing: 2.6px;
  }
  .band__tail {
    position: absolute; left: 527px; top: 306px; width: 88px; height: 29px;
    background: var(--white);
  }
  .band__mark {
    position: absolute; left: 480px; top: 301px;
    width: 38px; height: 38px; border-radius: 50%;
    background: var(--card); border: 3px solid var(--red);
  }

  .back-brand {
    position: absolute; left: 0; right: 0; top: 82px;
    display: flex; flex-direction: column; align-items: center; gap: 14px;
  }
  .back-brand__dot { width: 110px; height: 110px; border-radius: 50%; background: var(--red-bright); }
  .back-brand__name { color: var(--white); font-size: 30px; font-weight: 600; line-height: 1; }
  .tagline {
    position: absolute; left: 0; right: 0; top: 290px; text-align: center;
    color: var(--text-light); font-style: italic; font-size: 16.5px;
  }
</style>
</head>
<body>
<div class="canvas">

  <section class="card card--front">
    <div class="brand">
      <span class="brand__dot"></span>
      <span class="brand__name">PlateMarks</span>
    </div>

    <div class="divider"></div>

    <div class="contact">
      <p class="contact__name">DANIEL MARSH</p>
      <p class="contact__role">CEO/Founder</p>
      <p class="contact__address">4120 Linden Court<br>Fairview, Oregon 97024</p>
      <ul class="contact__list">
        <li class="contact__item">
          <svg viewBox="0 0 16 16" aria-hidden="true"><path d="M3.5 1l3 3-1.6 2a9 9 0 0 0 5.1 5.1l2-1.6 3 3-2 2.5C6.5 15 1 9.5 1 3z"/></svg>
          503 218 4471
        </li>
        <li class="contact__item">
          <svg viewBox="0 0 16 16" aria-hidden="true"><path d="M4 0h8a1 1 0 0 1 1 1v14a1 1 0 0 1-1 1H4a1 1 0 0 1-1-1V1a1 1 0 0 1 1-1zm1 2v10h6V2zm3 11a1 1 0 1 0 0 2 1 1 0 0 0 0-2z"/></svg>
          503 762 1085
        </li>
        <li class="contact__item">
          <svg viewBox="0 0 16 16" aria-hidden="true"><path d="M4 1h8v4H4zM1 6h14v7H1zm3 4h8v5H4z"/></svg>
          503 390 5526
        </li>
        <li class="contact__item">
          <svg viewBox="0 0 16 16" aria-hidden="true"><path d="M1 3h14v10H1zm1.5 1.5L8 9l5.5-4.5V4h-11z"/></svg>
          daniel@platemarks.com
        </li>
      </ul>
    </div>

    <div class="band"><span class="band__url">www.platemarks.com</span></div>
    <div class="band__tail"></div>
    <span class="band__mark"></span>
  </section>

  <section class="card card--back">
    <div class="back-brand">
      <span class="back-brand__dot"></span>
      <span class="back-brand__name">PlateMarks</span>
    </div>
    <p class="tagline">Honest kosher restaurant reviews, written by people who dine out</p>
  </section>

</div>
</body>
</html>
```